A new novel about the early days of The Marlows needs a book cover design

The title of the book is A LANTERN IN WINTER
The cover should also include "a novel" and "by Tom Holloway" Those can be together or separate.
The design element I'd like to incorporate is the iconic "Dock Wall" photo of The Marlows in 1960, which I've attached below. Since we're not sure if we can get the rights to the actual photo, it's probably best if the design merely references that photo, or distorts it in an interesting way. But it should be very clear that the book is about the Marlows.
The novel is in many ways based on that photo and evokes the city of Hamburg in 1960, which was gritty, raw, and sexually charged (as were The Marlows).
The tone of the novel is romantic, passionate, and very funny - but never broad and silly.

```html
<!DOCTYPE html>
<html lang="en">
<head>
<meta charset="utf-8">
<title>A Lantern in Winter — a novel by Tom Holloway</title>
<link rel="stylesheet" href="https://fonts.googleapis.com/css2?family=Bebas+Neue&family=Gelasio:ital@1&display=swap">
<style>
  :root {
    --ink: #000000;
    --stripe: #4a4a4c;
    --title: #ffdd00;
    --mark: #ffffff;
    --band-light: #3a3a3a;
    --band-dark: #141414;
  }
  html, body {
    margin: 0;
    padding: 0;
    width: 750px;
    height: 1200px;
    overflow: hidden;
    background: var(--ink);
  }
  .cover {
    position: relative;
    width: 750px;
    height: 1200px;
    overflow: hidden;
  }
  .cover-art {
    position: absolute;
    inset: 0;
    display: block;
  }
  .stripe { fill: var(--stripe); }
  .dash { fill: var(--mark); }
  .title-line {
    font-family: "Bebas Neue", "Oswald", sans-serif;
    font-size: 264px;
    fill: var(--title);
  }
  .byline {
    position: absolute;
    left: 0;
    right: 0;
    top: 1132px;
    margin: 0;
    text-align: center;
    font-family: "Gelasio", Georgia, serif;
    font-style: italic;
    font-weight: 400;
    font-size: 27px;
    color: var(--mark);
    letter-spacing: 0.2px;
  }
</style>
</head>
<body>
<main class="cover">
  <svg class="cover-art" width="750" height="1200" viewBox="0 0 750 1200" xmlns="http://www.w3.org/2000/svg">
    <defs>
      <linearGradient id="band-tone" x1="0" y1="0" x2="0" y2="1">
        <stop offset="0" stop-color="var(--band-light)"/>
        <stop offset="0.55" stop-color="#222222"/>
        <stop offset="1" stop-color="var(--band-dark)"/>
      </linearGradient>
      <pattern id="diagonal-stripes" patternUnits="userSpaceOnUse" width="332" height="1200"
               patternTransform="translate(215 0) skewX(25.6)">
        <rect class="stripe" x="0" y="0" width="165" height="1200"/>
      </pattern>
    </defs>

    <rect class="background" width="750" height="1200" fill="var(--ink)"/>
    <rect class="stripes" width="750" height="1200" fill="url(#diagonal-stripes)"/>

    <rect class="band-photo" x="0" y="339" width="750" height="521" fill="url(#band-tone)"
          role="img" aria-label="Black-and-white photo of The Marlows posing with guitars and drums in front of the Dock Wall, Hamburg, 1960"/>

    <g class="dashes dashes-top">
      <rect class="dash" x="172" y="87" width="54" height="18"/>
      <rect class="dash" x="261" y="87" width="54" height="18"/>
      <rect class="dash" x="350" y="87" width="54" height="18"/>
      <rect class="dash" x="439" y="87" width="54" height="18"/>
      <rect class="dash" x="528" y="87" width="54" height="18"/>
    </g>

    <g class="title" aria-label="A Lantern in Winter">
      <text class="title-line" x="377" y="371" text-anchor="middle">A</text>
      <text class="title-line" x="377" y="570" text-anchor="middle" textLength="394" lengthAdjust="spacingAndGlyphs">LANTERN</text>
      <text class="title-line" x="377" y="766" text-anchor="middle">IN</text>
      <text class="title-line" x="377" y="965" text-anchor="middle" textLength="406" lengthAdjust="spacingAndGlyphs">WINTER</text>
    </g>

    <g class="dashes dashes-bottom">
      <rect class="dash" x="172" y="1053" width="54" height="18"/>
      <rect class="dash" x="261" y="1053" width="54" height="18"/>
      <rect class="dash" x="350" y="1053" width="54" height="18"/>
      <rect class="dash" x="439" y="1053" width="54" height="18"/>
      <rect class="dash" x="528" y="1053" width="54" height="18"/>
    </g>
  </svg>

  <p class="byline">A novel by Tom Holloway</p>
</main>
</body>
</html>
```